Printed Circuit Board Company Web Site Design - Please see new file 82012 web design

We are a printed circuit board manufacturer. Need a company professional web site to allow our potential customers to know more about our background, capability and our products. The web site will contain three languages, which are Chinese, English and Japanese. Our audience are mainly electronic companies that procure printed circuit boards. I have a word document that have all the required text in all three languages. The final design should communicate the impression that we embrace quality, trustworthiness and long term partnership business principles.
We should have sections that allow us to post pictures of our facilities.
I have added the three files in three different languages.
Some of the information is below:
Background
RVT Global Limited (RVT) was set up in Hong Kong in 2007 by two Hong Kong entrepreneurs, Mr. Lau Fong and Mr. Tak Wai. We acquired the single sided printed circuit board factory located in Dongguan City, Guangdong Province, China, from Bolvane Corporation of the U.S. in 2007. In addition to RVT, Mr. Fong and Mr. Wai also own Harbor Dynamics Company Limited, a semiconductor company based in Hong Kong since 1997 with a total investment of over US$100 million. Harbor is engaged in the manufacturing of flexible substrates and MEMS assembly business.
RVT has been awarded TS 16949 and ISO14000 certificates since 2009 and 2004 respectively.
Business Principles
RVT Global Limited strives to be a professional top notched printed circuit board supplier. We embrace four “EXCELLENCE” principles, namely, excellence in quality, excellence in prices, excellence in services and excellence in on time delivery.
We approach each customer with a long-term partnership view that delivers the lowest ownership costs and highest total values to our customers. We customize quotations and solutions in order to allow our customers to win more businesses. We believe by thinking from our customers’ points of view we will be able to create a WIN-WIN relationship.
Customers
Due to our excellent quality, services and production systems, RVT Global Limited manage to service a number of large Japanese and US customers, which include:
Technical capability overview
Below is an overview of our current capability:
Target Market(s)
Electronic companies buyers
Industry/Entity Type
Business
Requirements
Must have
- Capability description
Should not have
- no cartoon

```html
<!DOCTYPE html>
<html lang="en">
<head>
<meta charset="utf-8">
<title>RVT Global Limited</title>
<link rel="stylesheet" href="https://fonts.googleapis.com/css2?family=Open+Sans:wght@400;600;700&family=Roboto:wght@400;500&display=swap">
<style>
:root{
  --bg:#f2f2f2;
  --green:#1f8a6e;
  --btn:#1e7d6a;
  --btn-alt:#357a6c;
  --dot:#1dbb5a;
  --text:#2b2b2b;
  --dark-bar:#5a5a5a;
  --field:#7d7d7d;
  --band:#d4d4d4;
  --footer:#333333;
}
*{box-sizing:border-box;margin:0;padding:0}
html,body{width:1062px;height:1200px;overflow:hidden}
body{position:relative;background:var(--bg);font-family:"Open Sans",sans-serif;color:var(--text)}
.abs{position:absolute}
.brand{left:104px;top:44px;color:var(--green);font-family:"Open Sans",sans-serif;font-weight:700;line-height:1}
.brand .mark{font-size:42px;letter-spacing:4px;display:block}
.brand .sub{font-size:16px;letter-spacing:1px;display:block;margin-top:6px;padding-left:10px}
.langs{left:823px;top:38px;display:flex;gap:9px}
.phone{left:823px;top:78px;font-size:14px;color:#444}
.nav{top:142px;left:0;width:1062px;height:22px;font-size:14.5px;font-weight:600;color:#333}
.nav a{position:absolute;text-decoration:none;color:inherit}
.nav .active{color:var(--green)}
.nav .auth{color:var(--green);display:flex;align-items:center;gap:4px}
.topbar{top:164px;left:0;width:1062px;height:10px;background:var(--dark-bar)}
.photo{left:123px;top:210px;width:361px;height:271px;background:linear-gradient(135deg,#cfd3d6 0%,#e8e6e2 45%,#b7bcc0 75%,#c9a28a 100%)}
.pager{left:268px;top:501px;display:flex;gap:8px}
.pager span{width:11px;height:11px;border:1.4px solid #444;border-radius:50%}
.pager span:first-child{background:#ddd}
h2{position:absolute;font-family:"Roboto",sans-serif;font-weight:400;font-size:22px;color:#222;display:flex;align-items:center;gap:4px}
h2::before{content:"";border-left:13px solid var(--btn-alt);border-top:8px solid transparent;border-bottom:8px solid transparent}
.copy{font-size:13.4px;line-height:16px}
.copy strong{color:var(--green);font-weight:600}
.btn{position:absolute;background:var(--btn);color:#fff;font-size:16px;border-radius:4px;display:flex;align-items:center;justify-content:center}
.caps{left:126px;top:580px;width:277px;list-style:none;font-size:13.8px}
.caps li{height:28.5px;border-bottom:2px solid var(--green);display:flex;align-items:center;gap:5px}
.caps li::before{content:"";width:11px;height:11px;border-radius:50%;background:var(--dot)}
.field{left:104px;width:334px;height:31px;background:var(--field);color:#fff;font-size:13px;font-weight:700;padding-left:9px;display:flex;align-items:center}
.principles{left:528px;list-style:none;font-size:15px;font-weight:600;color:#333}
.principles li{position:absolute;white-space:nowrap;display:flex;align-items:center;gap:16px}
.principles li::before{content:"";width:11px;height:11px;border-radius:50%;background:var(--dot)}
.clients{top:1019px;left:0;width:1062px;height:127px;background:var(--band)}
.clients span{position:absolute;font-family:"Roboto",sans-serif;font-weight:500;font-size:19px;color:#3a3a3a;transform:translateX(-50%);white-space:nowrap}
.footer{top:1146px;left:0;width:1062px;height:54px;background:var(--footer);color:#fff;display:flex;justify-content:center;align-items:center;font-size:14.5px}
.footer a{color:#fff;text-decoration:none;padding:0 12px}
.footer i{display:inline-block;width:2px;height:18px;background:#fff}
</style>
</head>
<body>

<div class="abs brand"><span class="mark">RVT</span><span class="sub">Global Limited</span></div>

<div class="abs langs" aria-label="Language selection">
  <svg width="30" height="30" viewBox="0 0 30 30" aria-label="Chinese"><circle cx="15" cy="15" r="14" fill="#d52b1e"/><circle cx="10" cy="10" r="3" fill="#f6d21c"/></svg>
  <svg width="30" height="30" viewBox="0 0 30 30" aria-label="English"><circle cx="15" cy="15" r="14" fill="#1f3f8f"/><path d="M15 1v28M1 15h28" stroke="#fff" stroke-width="6"/><path d="M15 1v28M1 15h28" stroke="#c8102e" stroke-width="3"/></svg>
  <svg width="30" height="30" viewBox="0 0 30 30" aria-label="Japanese"><circle cx="15" cy="15" r="14" fill="#fff" stroke="#ccc"/><circle cx="15" cy="15" r="6" fill="#d01c2c"/></svg>
</div>
<div class="abs phone">(02) 555- 01934</div>

<nav class="abs nav">
  <a class="active" style="left:103px">Home</a>
  <a style="left:236px">Products</a>
  <a style="left:379px">Services</a>
  <a style="left:519px">About Us</a>
  <a style="left:670px">Contact</a>
  <a class="auth" style="left:777px"><svg width="17" height="15" viewBox="0 0 17 15"><rect width="17" height="15" rx="2" fill="#555"/><path d="M4 8h7M9 6l2 2-2 2" stroke="#fff" stroke-width="1.5" fill="none"/></svg>LOG IN</a>
  <a class="auth" style="left:858px"><svg width="17" height="17" viewBox="0 0 17 17"><rect width="17" height="17" rx="2" fill="#555"/><path d="M11 5H7a2 2 0 0 0 0 4h3a2 2 0 0 1 0 4H6" stroke="#fff" stroke-width="1.8" fill="none"/></svg>SIGN UP</a>
</nav>
<div class="abs topbar"></div>

<div class="abs photo" role="img" aria-label="Factory floor with circuit board processing machines"></div>
<div class="abs pager"><span></span><span></span><span></span><span></span></div>

<h2 style="left:528px;top:200px">Background</h2>
<p class="abs copy" style="left:528px;top:243px;width:405px">RVT Global Limited (RVT) was set up in Hong Kong in 2007 by two Hong Kong entrepreneurs,&nbsp; Mr. Lau Fong and Mr. Tak Wai.&nbsp; We acquired the single sided printed circuit board factory located in Dongguan City, Guangdong Province, China, from Bolvane Corporation of the U.S. in 2007. In addition to RVT, Mr. Fong and Mr. Wai also own <strong>Harbor Dynamics Company Limited</strong>,&nbsp; a semiconductor company based in Hong Kong since 1997 with a total investment of over US$100 million.&nbsp; Harbor is engaged in the manufacturing of flexible substrates and the assembly of <strong>Micro Electro Mechanical Systems</strong> (MEMS).</p>
<p class="abs copy" style="left:528px;top:434px;width:405px">RVT has been awarded TS 16949 and ISO14000 certificates since 2009 and 2004 respectively.</p>
<div class="btn" style="left:528px;top:482px;width:109px;height:33px">Learn More</div>

<h2 style="left:103px;top:538px">Technical capability overview</h2>
<ul class="abs caps">
  <li>Raw Materials</li>
  <li>Plating</li>
  <li>Printing Processes</li>
  <li>Punching And CNC Process</li>
  <li>V-Cut</li>
  <li>Surface Finishing</li>
  <li>Specification for carbon</li>
</ul>
<div class="btn" style="left:97px;top:797px;width:116px;height:29px;background:var(--btn-alt);font-size:17px">Learn More</div>

<h2 style="left:103px;top:846px">Newsletter</h2>
<div class="abs field" style="top:894px">Name</div>
<div class="abs field" style="top:934px">Tel</div>
<div class="abs field" style="top:974px">Email</div>

<h2 style="left:527px;top:538px">Business Principles</h2>
<p class="abs copy" style="left:527px;top:594px;width:400px">RVT Global Limited strives to be a professional top notched printed circuit board supplier. We embrace four “EXCELLENCE” principles.</p>
<ul class="abs principles" style="top:0">
  <li style="top:658px">excellence in quality</li>
  <li style="top:706px">excellence in prices</li>
  <li style="top:752px">excellence in services</li>
  <li style="top:796px">excellence in on time delivery</li>
</ul>
<p class="abs copy" style="left:528px;top:834px;width:410px">We approach each customer with a long-term partnership view that delivers the lowest ownership costs and highest total values to our customers.&nbsp; We customize quotations and solutions in order to allow our customers to win more businesses.&nbsp; We believe by thinking from our customers’ points of view we will be able to create a WIN-WIN relationship.</p>
<div class="btn" style="left:524px;top:967px;width:116px;height:29px;background:var(--btn-alt);font-size:17px">Learn More</div>

<section class="abs clients" aria-label="Customers">
  <span style="left:221px;top:20px">Norvale Systems</span>
  <span style="left:374px;top:20px">Keltor</span>
  <span style="left:470px;top:20px">Arvion</span>
  <span style="left:590px;top:20px">Sorano Motor</span>
  <span style="left:700px;top:20px">Quenta</span>
  <span style="left:782px;top:20px">Pellico</span>
  <span style="left:885px;top:20px">Velmira</span>
  <span style="left:155px;top:73px">Kazuri</span>
  <span style="left:325px;top:73px">Linfeng Tech</span>
  <span style="left:470px;top:73px">Orimex</span>
  <span style="left:597px;top:73px">Haruno</span>
  <span style="left:731px;top:73px">Drevon</span>
  <span style="left:882px;top:73px">Brennholt</span>
</section>

<footer class="abs footer">
  <a>Home</a><i></i><a>Products</a><i></i><a>Services</a><i></i><a>About Us</a><i></i><a>Contact</a>
</footer>

</body>
</html>
```